Narvelo - Human Capital Consultancy Business Cards

We need a business card design for a new professional services consulting company which is focused on People, Performance, Profit. Hence the company name "Narvelo Pty Ltd". We intend to work with organisations predominantly on achieving optimal business performance through it's people. Developing both individual and organisational capability through effective learning and talent management strategies. We also plan to offer leadership programs which look at how people can utilise wellness, mindfulness and resilience to enable them and their teams to perform more effectively. We are looking for something quite dynamic, even sporty looking rather than a staid'professional services' look. Please see logo attached.

Leadership

```html
<!DOCTYPE html>
<html lang="en">
<head>
<meta charset="utf-8">
<title>Narvelo Business Card Design</title>
<link rel="stylesheet" href="https://fonts.googleapis.com/css2?family=Ubuntu:wght@400;500;700&family=Comfortaa:wght@600;700&display=swap">
<style>
  :root {
    --page: #e9eaec;
    --card: #f7f7f8;
    --card-edge: #e4e5e8;
    --band-dark: #2a4ea6;
    --band-light: #4ba9df;
    --notch: #3a3d44;
    --logo-grey: #77787c;
    --text: #3b3c40;
    --orange: #f28a1a;
    --icon: #2f6fb3;
  }
  * { box-sizing: border-box; margin: 0; padding: 0; }
  html, body { width: 1200px; height: 861px; overflow: hidden; }
  body {
    background: var(--page);
    font-family: "Ubuntu", sans-serif;
    color: var(--text);
    position: relative;
  }
  .card {
    position: absolute;
    top: 265px;
    width: 540px;
    height: 330px;
    border-radius: 14px;
    background: linear-gradient(160deg, #ffffff 0%, var(--card) 55%, var(--card-edge) 100%);
    box-shadow: 0 10px 28px rgba(0,0,0,0.18);
    overflow: hidden;
  }
  .card--front { left: 40px; }
  .card--back { left: 620px; }
  .card__texture {
    position: absolute; inset: 0;
    background: linear-gradient(135deg, rgba(220,222,228,0.35), rgba(255,255,255,0) 60%);
  }
  .card__bands { position: absolute; inset: 0; }
  .brand {
    position: absolute; left: 0; right: 0;
    display: flex; justify-content: center; align-items: center; gap: 10px;
  }
  .brand__dot { border-radius: 50%; background: var(--orange); }
  .brand__name { font-family: "Ubuntu", sans-serif; font-weight: 700; color: var(--logo-grey); line-height: 1; }
  .tagline {
    position: absolute; left: 0; right: 0; text-align: center;
    font-family: "Ubuntu", sans-serif; color: var(--text); white-space: nowrap;
  }
  .web-large {
    position: absolute; left: 0; right: 0; text-align: center;
    font-family: "Comfortaa", sans-serif; font-weight: 700; color: var(--orange); white-space: nowrap;
  }
  .card--front .brand { top: 78px; }
  .card--front .brand__dot { width: 34px; height: 34px; }
  .card--front .brand__name { font-size: 64px; letter-spacing: 1px; }
  .card--front .tagline { top: 200px; font-size: 23px; }
  .card--front .web-large { top: 248px; font-size: 27px; }

  .card--back .brand { top: 44px; }
  .card--back .brand__dot { width: 18px; height: 18px; }
  .card--back .brand__name { font-size: 34px; }
  .card--back .tagline { top: 108px; font-size: 12.5px; }
  .person__name {
    position: absolute; top: 140px; left: 0; right: 0; text-align: center;
    font-family: "Comfortaa", sans-serif; font-weight: 700; font-size: 30px; color: var(--orange); white-space: nowrap;
  }
  .person__role {
    position: absolute; top: 184px; left: 0; right: 0; text-align: center;
    font-weight: 500; font-size: 18px; color: var(--text);
  }
  .contacts {
    position: absolute; top: 225px; left: 80px; right: 50px;
    display: grid; grid-template-columns: 240px 1fr; row-gap: 10px;
    list-style: none;
  }
  .contact { display: flex; align-items: center; gap: 8px; font-size: 17px; white-space: nowrap; }
  .contact--small { font-size: 15px; }
  .contact__icon { width: 24px; height: 24px; flex: none; }
</style>
</head>
<body>

  <section class="card card--front" aria-label="Business card front">
    <div class="card__texture" role="img" aria-label="Faint diamond lattice texture"></div>
    <svg class="card__bands" width="540" height="330" viewBox="0 0 540 330" aria-hidden="true">
      <defs>
        <linearGradient id="bandFront" x1="0" y1="0" x2="0" y2="1">
          <stop offset="0" stop-color="#2a4ea6"/>
          <stop offset="1" stop-color="#4ba9df"/>
        </linearGradient>
      </defs>
      <polygon points="0,0 26,0 26,110 82,170 26,230 26,330 0,330" fill="url(#bandFront)"/>
      <polygon points="0,150 18,170 0,190" fill="#3a3d44"/>
      <polygon points="540,0 514,0 514,110 462,170 514,230 514,330 540,330" fill="url(#bandFront)"/>
      <polygon points="540,150 524,170 540,190" fill="#3a3d44"/>
    </svg>
    <div class="brand"><span class="brand__dot"></span><span class="brand__name">Narvelo</span></div>
    <p class="tagline">Talent • Wellbeing • Results</p>
    <p class="web-large">www.narvelo.com</p>
  </section>

  <section class="card card--back" aria-label="Business card back">
    <div class="card__texture" role="img" aria-label="Faint diamond lattice texture"></div>
    <svg class="card__bands" width="540" height="330" viewBox="0 0 540 330" aria-hidden="true">
      <defs>
        <linearGradient id="bandBack" x1="0" y1="0" x2="0" y2="1">
          <stop offset="0" stop-color="#2a4ea6"/>
          <stop offset="1" stop-color="#4ba9df"/>
        </linearGradient>
      </defs>
      <polygon points="0,0 26,0 26,110 82,170 26,230 26,330 0,330" fill="url(#bandBack)"/>
      <polygon points="0,150 18,170 0,190" fill="#3a3d44"/>
      <polygon points="540,0 514,0 514,110 462,170 514,230 514,330 540,330" fill="url(#bandBack)"/>
      <polygon points="540,150 524,170 540,190" fill="#3a3d44"/>
    </svg>
    <div class="brand"><span class="brand__dot"></span><span class="brand__name">Narvelo</span></div>
    <p class="tagline">Talent • Wellbeing • Results</p>
    <h1 class="person__name">Name Surname</h1>
    <p class="person__role">Position</p>
    <ul class="contacts">
      <li class="contact">
        <svg class="contact__icon" viewBox="0 0 24 24" aria-hidden="true"><circle cx="12" cy="12" r="10.5" fill="none" stroke="#2f6fb3" stroke-width="2"/><rect x="10" y="5" width="4" height="14" rx="1" fill="#2f6fb3" transform="rotate(40 12 12)"/></svg>
        <span>+ 012345 6789</span>
      </li>
      <li class="contact contact--small">
        <svg class="contact__icon" viewBox="0 0 24 24" aria-hidden="true"><circle cx="12" cy="12" r="10.5" fill="none" stroke="#2f6fb3" stroke-width="2"/></svg>
        <span>NarveloHQ</span>
      </li>
      <li class="contact">
        <svg class="contact__icon" viewBox="0 0 24 24" aria-hidden="true"><circle cx="12" cy="12" r="10.5" fill="none" stroke="#2f6fb3" stroke-width="2"/><rect x="6.5" y="8" width="11" height="8" fill="#2f6fb3"/><polyline points="6.5,8 12,12.5 17.5,8" fill="none" stroke="#fff" stroke-width="1.2"/></svg>
        <span>name@narvelo.com</span>
      </li>
      <li class="contact contact--small">
        <svg class="contact__icon" viewBox="0 0 24 24" aria-hidden="true"><circle cx="12" cy="12" r="10.5" fill="none" stroke="#2f6fb3" stroke-width="2"/><rect x="6.5" y="7.5" width="11" height="8" fill="none" stroke="#2f6fb3" stroke-width="1.6"/><line x1="9" y1="17.5" x2="15" y2="17.5" stroke="#2f6fb3" stroke-width="1.6"/></svg>
        <span>www.narvelo.com</span>
      </li>
    </ul>
  </section>

</body>
</html>
```